Tavlune

I'd like new business card design options. I'll need to provide updated contact info although after the deign is complete. We are in IT, specifically in the data backup, archiving and disaster recovery verticals.

Business

```html
<!DOCTYPE html>
<html lang="en">
<head>
<meta charset="utf-8">
<title>Tavlune Business Card</title>
<link rel="stylesheet" href="https://fonts.googleapis.com/css2?family=Open+Sans:wght@400;600;700&display=swap">
<style>
  :root {
    --backdrop: #4b4541;
    --card: #0b0b0c;
    --brand-blue: #1f7fd6;
    --accent-blue: #2a8fe0;
    --silver: #c9ccd0;
    --text-light: #e8e8e8;
    --text-muted: #cfcfcf;
  }
  * { box-sizing: border-box; margin: 0; padding: 0; }
  html, body {
    width: 1200px; height: 900px; overflow: hidden;
    background: var(--backdrop);
    font-family: "Open Sans", Arial, sans-serif;
  }
  .stage {
    width: 1200px; height: 900px;
    display: flex; align-items: center; justify-content: center; gap: 40px;
  }
  .card {
    width: 540px; height: 310px;
    background: var(--card);
    position: relative;
    box-shadow: 0 10px 28px rgba(0,0,0,.45);
  }
  .brand { display: flex; align-items: center; gap: 10px; }
  .brand-dot {
    width: 48px; height: 48px; border-radius: 50%;
    background: var(--brand-blue);
  }
  .brand-name {
    font-weight: 700; font-size: 25px; letter-spacing: 5px;
    color: var(--brand-blue);
  }
  /* contact side */
  .card-contact .brand { position: absolute; left: 40px; top: 140px; }
  .divider {
    position: absolute; left: 278px; top: 58px;
    width: 1px; height: 190px; background: var(--accent-blue);
  }
  .contact { position: absolute; left: 300px; top: 62px; color: var(--text-light); }
  .person-name { font-size: 19px; font-weight: 400; color: var(--accent-blue); letter-spacing: .5px; line-height: 1.1; }
  .person-role { font-size: 13px; margin-bottom: 10px; }
  .contact-list { list-style: none; font-size: 13px; line-height: 20px; }
  .contact-list li { display: flex; align-items: center; gap: 8px; }
  .contact-list svg { width: 11px; height: 11px; fill: var(--accent-blue); flex: none; }
  .address { margin-top: 12px; font-size: 13px; line-height: 20px; color: var(--text-muted); }
  /* logo side */
  .card-logo { display: flex; align-items: center; justify-content: center; }
  .card-logo .brand-dot { width: 70px; height: 70px; }
  .card-logo .brand-name { font-size: 30px; letter-spacing: 7px; color: var(--silver); }
</style>
</head>
<body>
<main class="stage">
  <section class="card card-contact">
    <div class="brand">
      <span class="brand-dot"></span>
      <span class="brand-name">TAVLUNE</span>
    </div>
    <span class="divider"></span>
    <div class="contact">
      <p class="person-name">DANIEL HARROW</p>
      <p class="person-role">Managing Director</p>
      <ul class="contact-list">
        <li><svg viewBox="0 0 12 12"><path d="M1 3c0-1 1-2 2-2h6c1 0 2 1 2 2v1H8V3H4v1H1zM2 5h8l1 6H1z"/></svg>(044)555 0192</li>
        <li><svg viewBox="0 0 12 12"><path d="M3 0h6v12H3zM4 1v8h4V1z"/></svg>(044)555 0192</li>
        <li><svg viewBox="0 0 12 12"><path d="M0 2h12v8H0zM1 3l5 4 5-4z"/></svg>info@tavlune.com</li>
        <li><svg viewBox="0 0 12 12"><circle cx="6" cy="6" r="6"/></svg>www.tavlune.com</li>
      </ul>
      <p class="address">48 Fenwick Road,<br>Brightwater, 20417</p>
    </div>
  </section>
  <section class="card card-logo">
    <div class="brand">
      <span class="brand-dot"></span>
      <span class="brand-name">TAVLUNE</span>
    </div>
  </section>
</main>
</body>
</html>
```